Hello my name is Colin, I am Starting a business called Harbor Health and fitness and am in need of a memorable business card.
It is a personal training studio. I have added the logo that i would like to be on the left center om my business card. i would like room left up the top for a heading sentence such as. "Is your body shocking for all the wrong reasons". there must be room left on the right of the logo below the main heading for 3 sub headings.
then under those 3 headings and logo room for another larger heading eg. "give me a call and learn how to eat chocolate, drink bear and have great sex". in what room is left i would like to be used for my contact details, use I'm Colin Pettersby your fitness expert on the left then on the right Phone, Email and website space in at least 12 Point. Very specific i know :) now onto the back, for the back i would like an eye catching graphic and room for one main headline and 3 bullet points centered just write anything i will choose what to put in them when i pick a winner. Thank you very much for sticking through all of that :) i appreciate you taking the time to read it and hopefully undergo designing me a business card.
I can't wait to see the designs!

Target Market(s)

slightly more towards females although it would probably be best if it was targeted towards both sexes

Industry/Entity Type

Training

Requirements
Nice to have
• I would love to see if anyone could come up with a design that would really make my card stand out and be memorable.
Should not have
• tacky fitness photos of abs and muscles etc.

```html
<!DOCTYPE html>
<html lang="en">
<head>
<meta charset="utf-8">
<title>Harbor Health and Fitness – Stationery</title>
<link rel="stylesheet" href="https://fonts.googleapis.com/css2?family=Arimo:ital,wght@0,400;0,700;1,400&family=Jost:wght@400;500&display=swap">
<style>
  :root {
    --stage: #2c3192;
    --paper: #ffffff;
    --navy: #2b2f8f;
    --ink-blue: #14468a;
    --deep-blue: #0c4a86;
    --bright-blue: #1a9be6;
    --sky: #a9d9f6;
    --sky-pale: #cfe9fa;
    --window: #ececec;
    --label: #ffffff;
  }
  * { box-sizing: border-box; margin: 0; padding: 0; }
  html, body { width: 1200px; height: 737px; overflow: hidden; }
  body {
    position: relative;
    background: var(--stage);
    font-family: "Arimo", Arial, sans-serif;
    color: var(--navy);
  }
  .icons { position: absolute; width: 0; height: 0; }

  .piece-label {
    position: absolute;
    color: var(--label);
    font-size: 12px;
    white-space: nowrap;
  }

  /* brand name set as plain text */
  .brand { color: var(--ink-blue); font-family: "Jost", sans-serif; font-weight: 400; line-height: 1; white-space: nowrap; }
  .brand__name { display: block; font-size: 40px; letter-spacing: -0.5px; }
  .brand__tag { display: block; font-size: 10.5px; margin-top: 2px; padding-left: 38px; }
  .brand--small .brand__name { font-size: 34px; }
  .brand--small .brand__tag { font-size: 9px; padding-left: 30px; }

  .contact-list { list-style: none; font-size: 10px; line-height: 12.5px; color: var(--navy); white-space: nowrap; }
  .contact-list li { display: flex; align-items: center; gap: 4px; }
  .contact-list svg { width: 8px; height: 8px; flex: none; }

  .headline {
    font-family: "Jost", sans-serif;
    font-weight: 500;
    color: var(--navy);
    letter-spacing: -1.2px;
    line-height: 1.1;
    white-space: nowrap;
  }
  .cta-box {
    position: absolute;
    background: linear-gradient(100deg, var(--bright-blue), var(--deep-blue));
    color: var(--paper);
    font-size: 8px;
    line-height: 10.5px;
    padding: 10px 8px 0 22px;
    white-space: nowrap;
  }
  .cta-box::before {
    content: "";
    position: absolute;
    left: -6px; top: 20px;
    width: 12px; height: 12px;
    border-radius: 50%;
    background: var(--paper);
  }
  .cta-box::after {
    content: "";
    position: absolute;
    left: -1px; top: 23px;
    width: 4px; height: 4px;
    border-right: 1px solid var(--navy);
    border-top: 1px solid var(--navy);
    transform: rotate(45deg);
  }
  .web { position: absolute; font-size: 10px; font-weight: 700; color: var(--navy); white-space: nowrap; }
  .figure-fill { position: absolute; border-radius: 6px; }

  /* letterhead */
  .letterhead { position: absolute; left: 458px; top: 53px; width: 523px; height: 645px; background: var(--paper); }
  .letterhead .brand { position: absolute; left: 47px; top: 32px; }
  .letterhead .contact-list { position: absolute; left: 375px; top: 28px; }
  .letterhead .figure-fill { left: 170px; top: 425px; width: 240px; height: 200px; background: linear-gradient(180deg, var(--sky-pale), var(--sky)); opacity: .8; }
  .letterhead .web { left: 0; right: 0; bottom: 10px; text-align: center; }

  /* envelope */
  .envelope-flap { position: absolute; left: 40px; top: 140px; width: 674px; height: 132px; }
  .flap-url {
    position: absolute; left: 320px; top: 183px;
    color: var(--paper); font-size: 10px; font-weight: 700;
    transform: rotate(180deg);
    white-space: nowrap;
  }
  .envelope { position: absolute; left: 40px; top: 270px; width: 674px; height: 292px; background: var(--paper); }
  .envelope .brand { position: absolute; left: 40px; top: 36px; }
  .envelope .contact-list { position: absolute; left: 180px; top: 28px; }
  .envelope-window {
    position: absolute; left: 41px; top: 114px; width: 284px; height: 102px;
    border: 1px solid #cfcfcf; border-radius: 10px;
    background: linear-gradient(180deg, #f4f4f4, var(--window));
  }
  .envelope .figure-fill { left: 372px; top: 104px; width: 132px; height: 138px; background: var(--sky); }
  .envelope .headline { position: absolute; left: 519px; top: 101px; font-size: 20px; }
  .envelope .cta-box { left: 514px; top: 172px; width: 160px; height: 63px; }
  .envelope .web { left: 532px; top: 248px; }

  /* business card front */
  .card-front { position: absolute; left: 780px; top: 169px; width: 366px; height: 209px; background: var(--paper); }
  .card-front .brand { position: absolute; left: 32px; top: 24px; }
  .card-holder { position: absolute; left: 36px; top: 106px; white-space: nowrap; }
  .card-holder__name { font-size: 11px; font-weight: 700; }
  .card-holder__role { font-size: 9px; font-style: italic; margin-top: 2px; }
  .card-front .contact-list { position: absolute; left: 36px; top: 152px; }
  .card-front .headline { position: absolute; left: 212px; top: 27px; font-size: 19.5px; }
  .card-front .cta-box { left: 207px; top: 101px; width: 159px; height: 63px; }
  .card-front .web { left: 210px; top: 185px; }

  /* business card back */
  .card-back {
    position: absolute; left: 780px; top: 401px; width: 366px; height: 208px;
    background: linear-gradient(160deg, var(--ink-blue) 0%, #1770c2 45%, var(--deep-blue) 100%);
    overflow: hidden;
  }
  .sub-list { position: absolute; left: 52px; top: 32px; list-style: none; color: var(--paper); font-size: 12px; line-height: 22.5px; white-space: nowrap; }
  .card-back .figure-fill { left: 222px; top: 10px; width: 122px; height: 128px; background: linear-gradient(180deg, #b9d7ee, #8fb9df); }
  .card-back-band { position: absolute; left: 0; top: 140px; width: 100%; height: 51px; background: var(--paper); }
  .card-back-band .brand { position: absolute; left: 52px; top: 6px; }
  .card-back-band .brand--small .brand__name { font-size: 30px; }
  .band-arrow { position: absolute; left: 204px; top: 18px; width: 14px; height: 14px; }
  .band-cta { position: absolute; left: 227px; top: 10px; font-size: 8px; line-height: 10.5px; color: var(--navy); font-weight: 700; white-space: nowrap; }
  .card-back-strip { position: absolute; left: 0; top: 191px; width: 100%; height: 17px; background: var(--bright-blue); }
</style>
</head>
<body>

<svg class="icons" aria-hidden="true">
  <symbol id="icon-phone" viewBox="0 0 10 10">
    <circle cx="5" cy="5" r="4.4" fill="none" stroke="#1a9be6" stroke-width="1"/>
    <path d="M3.3 2.8c.4-.3.7-.2.9.2l.3.6c.1.3 0 .5-.2.6l-.2.2c.3.6.7 1 1.3 1.3l.2-.2c.2-.2.4-.2.6-.1l.6.3c.4.2.4.5.2.9-.5.6-1.3.6-2.2 0-1-.6-1.6-1.4-1.9-2.3-.1-.6 0-1.1.4-1.5z" fill="#2b2f8f"/>
  </symbol>
  <symbol id="icon-mail" viewBox="0 0 10 10">
    <circle cx="5" cy="5" r="4.4" fill="none" stroke="#1a9be6" stroke-width="1"/>
    <rect x="2.6" y="3.4" width="4.8" height="3.2" fill="none" stroke="#2b2f8f" stroke-width=".8"/>
    <path d="M2.6 3.4 5 5.2l2.4-1.8" fill="none" stroke="#2b2f8f" stroke-width=".8"/>
  </symbol>
</svg>

<p class="piece-label" style="left:491px;top:27px;">Letterhead :&nbsp; US letter</p>
<p class="piece-label" style="left:1019px;top:144px;">Bizcard Front</p>
<p class="piece-label" style="left:1029px;top:626px;">Bizcard Back</p>
<p class="piece-label" style="left:249px;top:578px;">Envelope: #10 size</p>

<!-- Letterhead -->
<section class="letterhead">
  <div class="brand"><span class="brand__name">Harbor</span><span class="brand__tag">Health and Fitness</span></div>
  <ul class="contact-list">
    <li><svg><use href="#icon-phone"/></svg>408-555-0142</li>
    <li><svg><use href="#icon-phone"/></svg>XXX-XXX-XXXX</li>
    <li><svg><use href="#icon-phone"/></svg>408-555-0187</li>
    <li><svg><use href="#icon-mail"/></svg>colin@harborhealthfit.com</li>
  </ul>
  <div class="figure-fill" role="img" aria-label="Faint silhouette of a woman running on a treadmill"></div>
  <p class="web">www.harborhealthfit.com</p>
</section>

<!-- Envelope -->
<svg class="envelope-flap" viewBox="0 0 674 132" aria-hidden="true">
  <defs>
    <linearGradient id="flap-fill" x1="0" y1="1" x2="1" y2="0">
      <stop offset="0" stop-color="#1c8fe2"/>
      <stop offset=".35" stop-color="#0f5597"/>
      <stop offset="1" stop-color="#0c4a86"/>
    </linearGradient>
  </defs>
  <path d="M0 132 L22 96 Q30 84 48 80 C150 40 240 8 350 5 C470 8 560 50 640 84 Q660 92 674 132 Z" fill="url(#flap-fill)"/>
</svg>
<p class="flap-url">www.harborhealthfit.com</p>

<section class="envelope">
  <div class="brand brand--small"><span class="brand__name">Harbor</span><span class="brand__tag">Health and Fitness</span></div>
  <ul class="contact-list">
    <li><svg><use href="#icon-phone"/></svg>408-555-0142</li>
    <li><svg><use href="#icon-phone"/></svg>XXX-XXX-XXXX</li>
    <li><svg><use href="#icon-phone"/></svg>408-555-0187</li>
    <li><svg><use href="#icon-mail"/></svg>colin@harborhealthfit.com</li>
  </ul>
  <div class="envelope-window"></div>
  <div class="figure-fill" role="img" aria-label="Silhouette of a woman running on a treadmill"></div>
  <h2 class="headline">Is your body<br>shocking for all the<br>wrong reasons</h2>
  <p class="cta-box">Give me a call and learn how<br>to eat chocolate, drink bear<br>and have great sex</p>
  <p class="web">www.harborhealthfit.com</p>
</section>

<!-- Business card front -->
<section class="card-front">
  <div class="brand"><span class="brand__name">Harbor</span><span class="brand__tag">Health and Fitness</span></div>
  <div class="card-holder">
    <p class="card-holder__name">Colin Pettersby</p>
    <p class="card-holder__role">FITNESS EXPERT</p>
  </div>
  <ul class="contact-list">
    <li><svg><use href="#icon-phone"/></svg>408-555-0142</li>
    <li><svg><use href="#icon-phone"/></svg>XXX-XXX-XXXX</li>
    <li><svg><use href="#icon-phone"/></svg>408-555-0187</li>
    <li><svg><use href="#icon-mail"/></svg>colin@harborhealthfit.com</li>
  </ul>
  <h2 class="headline">Is your body<br>shocking for all the<br>wrong reasons</h2>
  <p class="cta-box">Give me a call and learn how<br>to eat chocolate, drink bear<br>and have great sex</p>
  <p class="web">www.harborhealthfit.com</p>
</section>

<!-- Business card back -->
<section class="card-back">
  <ul class="sub-list">
    <li>1 sub headings</li>
    <li>2 sub headings</li>
    <li>3 sub headings</li>
  </ul>
  <div class="figure-fill" role="img" aria-label="Silhouette of a woman running on a treadmill"></div>
  <div class="card-back-band">
    <div class="brand brand--small"><span class="brand__name">Harbor</span><span class="brand__tag">Health and Fitness</span></div>
    <svg class="band-arrow" viewBox="0 0 14 14" aria-hidden="true">
      <circle cx="7" cy="7" r="7" fill="#2b2f8f"/>
      <path d="M5.8 4.3 8.5 7l-2.7 2.7" fill="none" stroke="#fff" stroke-width="1.4"/>
    </svg>
    <p class="band-cta">Give me a call and learn how<br>to eat chocolate, drink bear<br>and have great sex</p>
  </div>
  <div class="card-back-strip"></div>
</section>

</body>
</html>
```